Web Design Project - Velvet Hour service

Shall be a social community to set private dates for Velvet Hour service.
Main function is to
* Search / View / Contact / Recommend profiles
* Contact profiles

Industry/Entity Type

Escort

```html
<!DOCTYPE html>
<html lang="en">
<head>
<meta charset="utf-8">
<title>Velvet Hour — Get In Touch</title>
<link rel="stylesheet" href="https://fonts.googleapis.com/css2?family=Cormorant+Garamond:ital,wght@0,500;1,500&family=Tinos&family=Arimo:wght@400;700&display=swap">
<style>
  :root {
    --bg: #4a3b25;
    --bg-dark: #2b2418;
    --gold: #d6c79c;
    --gold-deep: #c2ad78;
    --frame: #6b5a38;
    --field: #5a4622;
    --field-line: #736653;
    --label-bg: #3c301e;
    --label-text: #e2d5ad;
    --pink: #e3177e;
    --pink-text: #f5c8de;
    --cream: #f1e2a3;
    --cream-text: #b2a070;
    --sage: #7f8a79;
    --sage-text: #2e3028;
    --umber: #6a5944;
    --umber-text: #dcd3c2;
    --submit-bg: #7b6142;
    --submit-text: #cdb88d;
    --footer-text: #f2ecdc;
  }
  * { margin: 0; padding: 0; box-sizing: border-box; }
  html, body { width: 1200px; height: 900px; overflow: hidden; }
  body {
    position: relative;
    background: radial-gradient(circle at 50% 40%, #514129 0%, var(--bg) 55%, #433520 100%);
    font-family: "Tinos", Georgia, serif;
    color: var(--label-text);
  }
  .brand-photo {
    position: absolute; left: 0; top: 0; width: 56px; height: 155px;
    background: linear-gradient(180deg, #3a3430 0%, #b9b2a8 45%, #d8d2c8 100%);
    border-radius: 20px 20px 8px 8px;
  }
  .brand-name {
    position: absolute; left: 62px; top: 0; width: 160px;
    font-family: "Cormorant Garamond", Georgia, serif; font-weight: 500;
    font-size: 36px; line-height: 46px; color: var(--gold);
  }
  .brand-name span { display: block; }
  .brand-name span + span { padding-left: 28px; }

  .main-nav { position: absolute; left: 535px; top: 0; display: flex; gap: 5px; }
  .main-nav a {
    display: block; width: 163px; height: 54px; line-height: 54px; text-align: center;
    text-decoration: none; border-radius: 0 0 8px 8px; border: 2px solid rgba(0,0,0,.35);
    border-top: none; font-size: 32px;
  }
  .nav-vip { background: var(--pink); color: var(--pink-text); font-family: "Arimo", Arial, sans-serif; }
  .nav-register { background: var(--cream); color: var(--cream-text); font-family: "Arimo", Arial, sans-serif; }
  .nav-about { background: var(--sage); color: var(--sage-text); font-family: "Tinos", Georgia, serif; }
  .nav-services { background: var(--umber); color: var(--umber-text); font-family: "Arimo", Arial, sans-serif; font-weight: 700; }

  .hero-photo {
    position: absolute; left: 400px; top: 62px; width: 432px; height: 356px;
    background: linear-gradient(90deg, #c99c7e 0%, #b27a55 35%, #a8714c 55%, #6b6b6b 75%, #2e2e2e 100%);
    border-radius: 90px 90px 6px 6px;
    opacity: .9;
  }
  .slider-btn {
    position: absolute; top: 231px; width: 97px; height: 60px; background: var(--bg-dark);
    font-family: "Cormorant Garamond", Georgia, serif; font-style: italic; font-size: 36px;
    color: var(--gold); line-height: 56px; text-align: center; text-decoration: none;
  }
  .slider-prev { left: 0; }
  .slider-next { right: 0; }

  .contact-title {
    position: absolute; left: 125px; top: 390px;
    font-family: "Cormorant Garamond", Georgia, serif; font-style: italic; font-size: 40px;
    color: var(--gold); letter-spacing: 1px;
  }
  .contact-arrow { position: absolute; left: 82px; top: 412px; }

  .contact-form {
    position: absolute; left: 305px; top: 437px; width: 659px; height: 389px;
    border: 4px solid var(--frame);
  }
  .form-row { position: absolute; left: 14px; height: 48px; }
  .form-row label {
    position: absolute; left: 6px; top: 0; height: 44px; padding: 0 12px;
    background: var(--label-bg); border-radius: 10px;
    font-size: 28px; line-height: 44px; color: var(--label-text); white-space: nowrap;
  }
  .form-row input, .form-row textarea {
    position: absolute; left: 166px; top: -4px; width: 424px; height: 46px;
    background: var(--field); border: none; border-top: 4px solid var(--field-line);
    border-radius: 3px; outline: none; resize: none; color: var(--label-text);
  }
  .submit-btn {
    position: absolute; left: 530px; top: 348px; width: 114px; height: 36px;
    background: var(--submit-bg); border: none; border-radius: 14px;
    font-family: "Cormorant Garamond", Georgia, serif; font-style: italic; font-size: 34px;
    color: var(--submit-text); line-height: 30px;
  }

  .social-links { position: absolute; left: 14px; top: 874px; display: flex; gap: 11px; }
  .social-links span { display: block; width: 29px; height: 26px; border-radius: 4px; background: var(--umber); }
  .copyright {
    position: absolute; left: 0; right: 0; top: 864px; text-align: center;
    font-size: 24px; color: var(--footer-text); word-spacing: 2px;
  }
  .copyright .gap { display: inline-block; width: 30px; }
</style>
</head>
<body>
  <header class="site-header">
    <div class="brand-photo" role="img" aria-label="Portrait photo of a male model"></div>
    <div class="brand-name"><span>Velvet</span><span>Hour</span></div>
    <nav class="main-nav">
      <a class="nav-vip" href="#">Vip List</a>
      <a class="nav-register" href="#">Register</a>
      <a class="nav-about" href="#">About Us</a>
      <a class="nav-services" href="#">Services</a>
    </nav>
  </header>

  <section class="hero-slider">
    <a class="slider-btn slider-prev" href="#">prev</a>
    <div class="hero-photo" role="img" aria-label="Photo of three shirtless male models"></div>
    <a class="slider-btn slider-next" href="#">next</a>
  </section>

  <section class="contact">
    <h2 class="contact-title">Get In Touch</h2>
    <svg class="contact-arrow" width="74" height="96" viewBox="0 0 74 96" aria-hidden="true">
      <path d="M26 4 C4 18 2 52 30 68 L30 56 L72 76 L30 94 L30 82 C-8 66 -4 20 26 4 Z" fill="var(--gold-deep)"/>
    </svg>
    <form class="contact-form">
      <div class="form-row" style="top:14px"><label>Name&nbsp; :</label><input type="text"></div>
      <div class="form-row" style="top:86px"><label>Email&nbsp;&nbsp; :</label><input type="email"></div>
      <div class="form-row" style="top:157px"><label>Phone&nbsp;&nbsp; :</label><input type="tel"></div>
      <div class="form-row" style="top:230px"><label>Subject&nbsp; :</label><input type="text"></div>
      <div class="form-row" style="top:302px"><label>Message :</label><textarea></textarea></div>
      <button class="submit-btn" type="button">Submit</button>
    </form>
  </section>

  <footer class="site-footer">
    <div class="social-links"><span></span><span></span></div>
    <p class="copyright">Copyright<span class="gap"></span>2011-12.VelvetHour.com.All rights are reserved</p>
  </footer>
</body>
</html>
```